KVO-Business Card Design

I need a modern, professional business card design that includes my logo as the main feature, maybe the entire background with the contact info overlaying or even contact info on the back and the logo full frontal

Neat and organized placement of contact information

Would like to see options in black and white

Target Market(s)

real estate Developers, Construction managers, business and home owners

Industry/Entity Type

Construction

Contact Information for Business Card

KVO Construction
Danny Ferrante
General Contractor

Office: 1-888-902-7315 Ext #1
Cell: 215-730-4162
Fax: 1-888-902-7315

Font styles to use
Serif

Requirements
Must have
• title
• office #
• cell #
• Email
• website
Nice to have
• fax

```html
<!DOCTYPE html>
<html lang="en">
<head>
<meta charset="utf-8">
<title>KVO Construction – Business Card</title>
<link rel="stylesheet" href="https://fonts.googleapis.com/css2?family=Open+Sans:ital,wght@0,400;0,600;0,700;1,400&display=swap">
<style>
  :root {
    --page-bg: #b9bfc1;
    --card-dark: #3a3a3a;
    --card-dark-edge: #2e2e2e;
    --card-light: #f1f1f1;
    --card-light-shade: #cfcfcf;
    --brand-green: #2f9a37;
    --title-green: #1f7f2a;
    --ink: #1f1f1f;
    --on-dark: #e9e9e9;
  }
  * { box-sizing: border-box; margin: 0; padding: 0; }
  html, body { width: 1200px; height: 900px; overflow: hidden; }
  body {
    background: var(--page-bg);
    font-family: "Open Sans", sans-serif;
    position: relative;
  }
  .card {
    position: absolute;
    left: 250px;
    width: 700px;
    height: 400px;
    border-radius: 4px;
    overflow: hidden;
    box-shadow: 0 6px 18px rgba(0,0,0,.25);
  }
  /* Front */
  .card-front {
    top: 35px;
    background: radial-gradient(ellipse at 50% 40%, #454545 0%, var(--card-dark) 55%, var(--card-dark-edge) 100%);
    display: flex;
    align-items: center;
    justify-content: center;
  }
  .brand-mark {
    display: flex;
    align-items: center;
    gap: 18px;
  }
  .brand-square {
    width: 34px;
    height: 34px;
    background: var(--brand-green);
  }
  .brand-name {
    font-weight: 700;
    font-size: 46px;
    letter-spacing: 1px;
    color: var(--brand-green);
  }
  /* Back */
  .card-back {
    top: 465px;
    background: linear-gradient(180deg, var(--card-light) 0%, #e2e2e2 40%, var(--card-light-shade) 62%);
  }
  .identity {
    position: absolute;
    left: 72px;
    top: 52px;
    padding-left: 14px;
    border-left: 1.5px solid #444;
  }
  .person-name {
    font-weight: 700;
    font-size: 27px;
    color: var(--ink);
    line-height: 1.1;
  }
  .person-title {
    font-weight: 600;
    font-size: 16px;
    color: var(--title-green);
    margin-top: 2px;
  }
  .skyline {
    position: absolute;
    left: 0;
    top: 118px;
    width: 700px;
    height: 132px;
    background: linear-gradient(180deg, rgba(58,58,58,0) 0%, rgba(58,58,58,.45) 45%, var(--card-dark) 100%);
  }
  .contact-band {
    position: absolute;
    left: 0;
    top: 250px;
    width: 700px;
    height: 150px;
    background: var(--card-dark);
  }
  .contact-list {
    position: absolute;
    list-style: none;
    color: var(--on-dark);
    font-size: 18px;
    white-space: nowrap;
  }
  .contact-list li {
    display: flex;
    align-items: center;
    gap: 12px;
    height: 30px;
  }
  .contact-list svg { width: 18px; height: 18px; flex: none; }
  .phones { left: 62px; top: 24px; font-style: italic; }
  .online { left: 300px; top: 30px; }
  .online li { height: 32px; }
  .corner-brand {
    position: absolute;
    right: 34px;
    top: 36px;
    width: 120px;
    display: flex;
    flex-direction: column;
    align-items: center;
    gap: 6px;
    text-align: center;
  }
  .corner-brand .brand-square { width: 16px; height: 16px; }
  .corner-brand .brand-name { font-size: 18px; line-height: 1.15; letter-spacing: .5px; }
</style>
</head>
<body>

<section class="card card-front" aria-label="Card front">
  <div class="brand-mark">
    <span class="brand-square"></span>
    <span class="brand-name">KVO Construction</span>
  </div>
</section>

<section class="card card-back" aria-label="Card back">
  <div class="identity">
    <p class="person-name">Danny Ferrante</p>
    <p class="person-title">General Contractor</p>
  </div>

  <div class="skyline" role="img" aria-label="City skyline silhouette with construction cranes and tall towers"></div>

  <div class="contact-band">
    <ul class="contact-list phones">
      <li>
        <svg viewBox="0 0 18 18" fill="none" stroke="currentColor" stroke-width="1.6"><rect x="5" y="2" width="8" height="14" rx="1.5"/><line x1="8" y1="13.5" x2="10" y2="13.5"/></svg>
        <span>215-730-4162</span>
      </li>
      <li>
        <svg viewBox="0 0 18 18" fill="currentColor"><path d="M2 6c0-2 3-3 7-3s7 1 7 3v1h-3V6H5v1H2z"/><rect x="4" y="8" width="10" height="7" rx="1"/></svg>
        <span>1-888-902-7315 Ext #1</span>
      </li>
      <li>
        <svg viewBox="0 0 18 18" fill="none" stroke="currentColor" stroke-width="1.6"><rect x="5" y="2" width="8" height="5"/><rect x="2" y="7" width="14" height="6" rx="1"/><rect x="5" y="11" width="8" height="5"/></svg>
        <span>1-888-902-7315</span>
      </li>
    </ul>

    <ul class="contact-list online">
      <li>
        <svg viewBox="0 0 18 18" fill="none" stroke="currentColor" stroke-width="1.4"><circle cx="9" cy="9" r="7"/><ellipse cx="9" cy="9" rx="3" ry="7"/><line x1="2" y1="9" x2="16" y2="9"/><line x1="3" y1="5.5" x2="15" y2="5.5"/><line x1="3" y1="12.5" x2="15" y2="12.5"/></svg>
        <span>www.example.com</span>
      </li>
      <li>
        <svg viewBox="0 0 18 18" fill="none" stroke="currentColor" stroke-width="1.5"><rect x="2" y="4" width="14" height="10"/><polyline points="2,4 9,10 16,4"/></svg>
        <span>example@example.com</span>
      </li>
    </ul>

    <div class="corner-brand">
      <span class="brand-square"></span>
      <span class="brand-name">KVO Construction</span>
    </div>
  </div>
</section>

</body>
</html>
```